Business card design for Allied Healthcare provider

We would like a design for front and back of business cards. The design must resonate with all levels of customers from patients, to other health providers and medical. Must also resonate with corporate customers

Target Market(s)

patients, medical practitioners, other health providers and corporate.

Industry/Entity Type

healthcare

Contact Information for Business Card

name, logo, phone and fax numbers, email, website

Requirements
Must have
• not allowing me to change this, but the card must be double sided!! Please take note
Nice to have
• a fresh yet bold design to catch attention.

```html
<!DOCTYPE html>
<html lang="en">
<head>
<meta charset="utf-8">
<title>Carewell business card — front and back</title>
<link href="https://fonts.googleapis.com/css2?family=Poppins:wght@400;500;600;700&display=swap" rel="stylesheet">
<style>
  :root {
    --navy: #1b2d58;
    --gold: #fbb424;
    --white: #ffffff;
    --muted: #2a2f3a;
    --stage: #d9dce2;
  }
  * { box-sizing: border-box; margin: 0; padding: 0; }
  html, body {
    width: 1200px; height: 900px; overflow: hidden;
    background: var(--stage);
    font-family: "Poppins", sans-serif;
  }
  .stage {
    width: 1200px; height: 900px;
    display: flex; flex-direction: column; align-items: center; justify-content: center;
    gap: 40px;
  }
  .card {
    position: relative;
    width: 700px; height: 400px;
    border-radius: 22px;
    overflow: hidden;
    box-shadow: 0 10px 30px rgba(20, 30, 60, 0.18);
  }

  /* Front */
  .card-front { background: var(--white); }
  .front-band { position: absolute; left: 0; bottom: 0; width: 100%; height: 40px; }
  .front-logo {
    position: absolute; left: 58px; top: 46px;
    display: flex; align-items: center; gap: 12px;
  }
  .logo-dot { width: 22px; height: 22px; border-radius: 50%; background: var(--gold); flex: none; }
  .logo-name {
    font-weight: 700; font-size: 44px; line-height: 1; letter-spacing: 0.5px;
    color: var(--navy);
  }
  .front-person { position: absolute; left: 58px; top: 132px; }
  .person-name {
    font-weight: 700; font-size: 26px; letter-spacing: 1px; line-height: 1.1;
    color: var(--navy);
  }
  .person-name .first { color: var(--gold); }
  .person-title { font-size: 15px; color: var(--muted); margin-top: 2px; }
  .title-rule { width: 40px; height: 2px; background: var(--gold); margin-top: 12px; }
  .contact-list { list-style: none; margin-top: 14px; }
  .contact-list li {
    display: flex; align-items: center; gap: 10px;
    font-size: 15px; color: var(--muted); line-height: 1.7;
  }
  .contact-list svg { width: 15px; height: 15px; fill: var(--navy); flex: none; }

  /* Back */
  .card-back {
    background: var(--navy);
    display: flex; flex-direction: column; align-items: center; justify-content: center;
  }
  .back-logo { display: flex; align-items: center; gap: 16px; }
  .back-logo .logo-name { color: var(--white); font-size: 72px; }
  .back-logo .logo-dot { width: 30px; height: 30px; }
  .tagline {
    margin-top: 10px; font-size: 24px; font-weight: 500; letter-spacing: 1px;
    color: var(--gold);
  }
</style>
</head>
<body>
<main class="stage">

  <section class="card card-front" aria-label="Business card front">
    <svg class="front-band" viewBox="0 0 700 40" preserveAspectRatio="none" aria-hidden="true">
      <polygon points="0,0 300,28 300,40 0,40" fill="var(--navy)"/>
      <polygon points="306,28 700,10 700,40 306,40" fill="var(--gold)"/>
    </svg>

    <div class="front-logo">
      <span class="logo-dot"></span>
      <span class="logo-name">carewell</span>
    </div>

    <div class="front-person">
      <h1 class="person-name"><span class="first">DANIEL</span> REYES</h1>
      <p class="person-title">CEO/Founder</p>
      <div class="title-rule"></div>
      <ul class="contact-list">
        <li>
          <svg viewBox="0 0 24 24" aria-hidden="true"><path d="M6.6 10.8a15.1 15.1 0 0 0 6.6 6.6l2.2-2.2a1 1 0 0 1 1-.25 11.4 11.4 0 0 0 3.6.57 1 1 0 0 1 1 1V20a1 1 0 0 1-1 1A17 17 0 0 1 3 4a1 1 0 0 1 1-1h3.5a1 1 0 0 1 1 1c0 1.25.2 2.45.57 3.6a1 1 0 0 1-.25 1z"/></svg>
          (01) 5550 1234
        </li>
        <li>
          <svg viewBox="0 0 24 24" aria-hidden="true"><path d="M6 2h12v6H6zM4 9h16a2 2 0 0 1 2 2v6h-4v5H6v-5H2v-6a2 2 0 0 1 2-2zm4 8v3h8v-3z"/></svg>
          (01) 5550 1235
        </li>
        <li>
          <svg viewBox="0 0 24 24" aria-hidden="true"><path d="M2 5h20v14H2zm2 2v.5l8 5 8-5V7zm0 2.8V17h16V9.8l-8 5z"/></svg>
          info@carewellhealth.com
        </li>
        <li>
          <svg viewBox="0 0 24 24" aria-hidden="true"><path d="M12 2a10 10 0 1 0 0 20 10 10 0 0 0 0-20zm0 2c.8 1.1 1.5 2.5 1.9 4h-3.8c.4-1.5 1.1-2.9 1.9-4zM4.3 14a8 8 0 0 1 0-4h3.4a16 16 0 0 0 0 4zm.8 2h3a15 15 0 0 0 1.3 3.9A8 8 0 0 1 5.1 16zm3-8h-3a8 8 0 0 1 4.3-3.9A15 15 0 0 0 8.1 8zM12 20c-.8-1.1-1.5-2.5-1.9-4h3.8c-.4 1.5-1.1 2.9-1.9 4zm2.3-6H9.7a14 14 0 0 1 0-4h4.6a14 14 0 0 1 0 4zm.3 5.9a15 15 0 0 0 1.3-3.9h3a8 8 0 0 1-4.3 3.9zM16.3 14a16 16 0 0 0 0-4h3.4a8 8 0 0 1 0 4zm2.6-6h-3a15 15 0 0 0-1.3-3.9A8 8 0 0 1 18.9 8z"/></svg>
          www.carewellhealth.com
        </li>
      </ul>
    </div>
  </section>

  <section class="card card-back" aria-label="Business card back">
    <div class="back-logo">
      <span class="logo-dot"></span>
      <span class="logo-name">carewell</span>
    </div>
    <p class="tagline">care · comfort · wellness</p>
  </section>

</main>
</body>
</html>
```